Web Page for Kestrel | ||
Marketing & Admin | ||
Energy | ||
will be www.kestrelfuels-example.com | ||
Kestrel Energy, LLC is a Exploration & Production company drilling oil and gas wells. | ||
Please us our Logo and colors that we had done at this site in Dec 2010. Do not use pictures of people. Would rather use our Logo and color than pictures. | ||
Cutting-Edge Unique/Creative Professional Conservative Exciting Sophisticated Corporate Elegant Traditional Masculine |
top | ||
www.vandrillex-example.com | ||
www.tarnwickog-example.com | ||
Just to see the look, you can use "selective" drilling rig pictures or pumping units but very few and not for all the the contest pages. We will have 2 additional pages at first but would like to be able to add additional in the future. | ||

```html
<!DOCTYPE html>
<html lang="en">
<head>
<meta charset="utf-8">
<title>Kestrel Energy LLC</title>
<link href="https://fonts.googleapis.com/css2?family=Arimo:wght@400;700&display=swap" rel="stylesheet">
<style>
:root{
  --page-bg:#dcdcdc;
  --sheet:#ffffff;
  --ink:#2b2b2b;
  --muted:#555555;
  --green:#0f7a3c;
  --green-dark:#0b5e2d;
  --nav-active:#1e1e1e;
  --orange:#d2501a;
  --orange-deep:#b63e10;
  --panel:#e4e4e4;
  --ticker:#262626;
  --footer:#d6d6d6;
}
*{box-sizing:border-box;margin:0;padding:0}
html,body{width:1200px;height:904px;overflow:hidden}
body{background:var(--page-bg);font-family:Arimo,Arial,sans-serif;color:var(--ink);position:relative}
.sheet{position:absolute;left:49px;top:10px;width:1095px;height:876px;background:var(--sheet)}
.brand{position:absolute;left:18px;top:16px;display:flex;align-items:center;gap:10px}
.brand-mark{width:74px;height:74px;border-radius:50%;background:var(--green-dark)}
.brand-name{font-size:30px;font-weight:700;color:#222;letter-spacing:-0.3px;white-space:nowrap}
.nav{position:absolute;right:10px;top:46px;height:42px;display:flex;background:var(--green)}
.nav a{color:#fff;text-decoration:none;font-weight:700;font-size:15px;padding:0 17px;line-height:42px;white-space:nowrap}
.nav a.active{background:var(--nav-active)}
.hero{position:absolute;left:17px;top:112px;width:810px;height:273px;
  background:linear-gradient(180deg,#3a2410 0%,#a14a12 35%,#e88a22 70%,#f4b04a 100%)}
.hero-title{position:absolute;left:0;top:70px;width:520px;padding:16px 28px;background:rgba(30,30,30,.72);
  color:#fff;font-size:40px;font-weight:700;line-height:1.08}
.ticker{position:absolute;left:17px;top:385px;width:810px;height:40px;background:var(--ticker);
  display:flex;align-items:center;justify-content:space-between;padding-right:20px;color:#fff;font-size:15px;font-weight:700;white-space:nowrap}
.ticker-label{background:#555;height:100%;padding:0 12px;line-height:40px}
.welcome{position:absolute;left:17px;top:440px;width:810px}
.welcome h2{color:var(--green);font-size:22px;margin-bottom:8px}
.welcome p{font-size:13.5px;line-height:1.45;color:var(--muted);text-align:justify}
.more{display:block;text-align:right;color:var(--orange-deep);font-size:12px;font-weight:700;margin-top:4px}
.side{position:absolute;left:837px;width:248px}
.press-head{top:104px;color:var(--green);font-size:21px;font-weight:700;white-space:nowrap}
.press{top:148px;height:277px;background:var(--panel);padding:10px 12px}
.press h4{color:var(--orange-deep);font-size:12px;margin:4px 0}
.press p{font-size:11.5px;color:var(--muted);font-weight:700;line-height:1.25;margin-bottom:8px}
.contact-head{top:438px;height:40px;background:var(--orange);color:#fff;text-align:center;font-size:21px;font-weight:700;line-height:40px}
.contact{top:478px;height:242px;background:var(--panel);padding:14px 10px;font-size:11.5px;font-weight:700;color:var(--muted);line-height:1.3}
.contact p{margin-bottom:12px}
.footer{position:absolute;left:0;bottom:0;width:100%;height:144px;background:var(--footer);
  text-align:center;font-size:15px;line-height:144px;color:#222}
</style>
</head>
<body>
<div class="sheet">
  <div class="brand"><div class="brand-mark"></div><div class="brand-name">Kestrel Energy LLC</div></div>
  <nav class="nav"><a class="active" href="#">Home</a><a href="#">About Us</a><a href="#">Corporate vision</a><a href="#">Products</a><a href="#">Services</a><a href="#">Contact Us</a></nav>

  <div class="hero" role="img" aria-label="Pumping units silhouetted against an orange sunset sky">
    <div class="hero-title">Kestrel Energy<br>announces some new<br>products.</div>
  </div>
  <div class="ticker"><div class="ticker-label">Stock Quote</div><span>584.35</span><span>Open 558.00</span><span>High 586.95</span><span>Low 558.00</span><span>01 Mar 12.00:00 AM EST</span></div>

  <section class="welcome">
    <h2>Welcome to our group</h2>
    <p>Through our energy reduction products and consulting services we are able to help our customers reduce their energy bills and carbon footprint. Although we work with all customers we specialize in the utility, retail, hospitality, commercial, and state energy program markets.</p>
    <p>We have evaluated many outstanding energy saving products and have spent a great deal of time determining the products and companies that provide the optimum value to the customer. The Kestrel Energy Group continually searches for products that provide our customers the greatest energy savings and return on their investment.</p>
    <p>We have evaluated many outstanding energy saving products and have spent a great deal of time determining the products and companies that provide the optimum value to the customer. The Kestrel Energy Group continually searches for products that provide our customers the greatest energy savings and return on their investment.</p>
    <a class="more" href="#">Learn more...</a>
  </section>

  <h3 class="side press-head">Latest Press Releases</h3>
  <div class="side press">
    <h4>January 2011</h4><p>The Kestrel Energy is an independent company specializing in energy efficiency products providing sales and consulting services.</p>
    <h4>January 2011</h4><p>The Kestrel Energy is an independent company specializing in energy efficiency products providing sales and consulting services.</p>
    <h4>January 2011</h4><p>The Kestrel Energy is an independent company specializing in energy efficiency products providing sales and consulting services.</p>
  </div>
  <div class="side contact-head">Contact Us</div>
  <div class="side contact">
    <p>Please contact us to discuss how Kestrel Energy Group can help you reach your energy reduction goals.</p>
    <p>Kestrel Energy LLC<br>xxxx Street South, #111<br>some place, some state 226001<br>Phone: xxx-xxx-xxxx<br>Fax: xxx-xxx-xxxx<br>email: info@kestrelfuels-example.com</p>
  </div>

  <footer class="footer">© 2001 - 2011 Kestrel Energy. All Rights Reserved. Terms of Use | Privacy Statement | Site Map | Site Feedback</footer>
</div>
</body>
</html>
```